App Design for quiz app (casual gaming app)

We need an design & logo for our quiz app. Its a simple quiz app, where you pick up a category, answer three questions out of this category. After this an opponent is assigned to your game, and has to answer the same three questions. After this first round is finished, it's the opponents turn to choose a new category and answer three questions out of this category. Now it's your turn to answer the same three questions. With this done, the 2nd round is finished. One game has seven rounds.
Please find attached the balsamiq project. For all of you, do not have balsamiq, please find also the mockups as pdf.
Final delivery should be psd files
Target Market(s)
Casual Games

```html
<!DOCTYPE html>
<html lang="en">
<head>
<meta charset="utf-8">
<title>Quiz App – Game Overview Screens</title>
<link rel="stylesheet" href="https://fonts.googleapis.com/css2?family=Fredoka:wght@500;600;700&family=Helvetica+Neue&display=swap">
<style>
  :root {
    --canvas-bg: #1e1e1e;
    --screen-top: #4a0a8c;
    --screen-mid: #5b137e;
    --screen-low: #2a1d4e;
    --screen-foot: #10252f;
    --row-a: #611784;
    --row-b: #53116f;
    --round-text: #62dbe6;
    --category-text: #3ccaa2;
    --score-bg: #12c47a;
    --score-text: #0b3d2a;
    --hex-green: #17b77b;
    --hex-red: #e8473f;
    --hex-empty: #4bbcc9;
    --avatar-ring: #24c7b5;
    --avatar-fill-a: #56d9e6;
    --avatar-fill-b: #2aa7b9;
    --stripe: #7a3fd0;
    --white: #ffffff;
    --button-a: #f2426e;
    --button-b: #e3295a;
    --button-text: #2a0a1a;
  }
  * { box-sizing: border-box; margin: 0; padding: 0; }
  html, body { width: 1200px; height: 1143px; overflow: hidden; background: var(--canvas-bg); }
  body { position: relative; font-family: "Fredoka", "Arial Rounded MT Bold", sans-serif; }

  .screen {
    position: absolute; top: 175px; width: 423px; height: 747px; overflow: hidden;
    background: linear-gradient(180deg, var(--screen-top) 0%, var(--screen-mid) 45%, var(--screen-low) 82%, var(--screen-foot) 100%);
  }
  .screen--left { left: 94px; }
  .screen--right { left: 673px; }

  .status-bar {
    position: absolute; top: 0; left: 0; right: 0; height: 27px;
    display: flex; align-items: center; justify-content: space-between;
    padding: 0 9px 0 11px; color: var(--white);
    font-family: "Helvetica Neue", Helvetica, Arial, sans-serif; font-size: 15px;
  }
  .status-bar__time { position: absolute; left: 50%; transform: translateX(-50%); }
  .status-bar__wifi { position: absolute; left: 137px; top: 6px; }
  .status-bar__battery { display: flex; align-items: center; gap: 5px; }

  .header-stripes { position: absolute; left: 0; top: 150px; width: 423px; height: 60px; }

  .avatar {
    position: absolute; width: 102px; height: 114px;
    clip-path: polygon(50% 0, 100% 25%, 100% 75%, 50% 100%, 0 75%, 0 25%);
    background: var(--avatar-ring);
  }
  .avatar__portrait {
    position: absolute; inset: 5px;
    clip-path: polygon(50% 0, 100% 25%, 100% 75%, 50% 100%, 0 75%, 0 25%);
    background: radial-gradient(circle at 50% 40%, var(--avatar-fill-a), var(--avatar-fill-b));
  }
  .avatar--one { left: 40px; top: 52px; }
  .avatar--two { left: 280px; top: 40px; }

  .scoreboard { position: absolute; left: 141px; top: 77px; width: 138px; height: 50px; }
  .score {
    position: absolute; top: 0; width: 53px; height: 46px;
    background: var(--score-bg); color: var(--score-text);
    font-size: 33px; font-weight: 700; line-height: 46px; text-align: center;
    transform: skewY(-3deg);
  }
  .score--one { left: 0; top: 4px; }
  .score--two { left: 84px; top: 0; }
  .score-colon { position: absolute; left: 65px; top: 6px; color: var(--white); font-size: 30px; font-weight: 700; }

  .player-name {
    position: absolute; color: var(--white); font-size: 22px; font-weight: 700;
    transform: rotate(-4deg);
  }
  .player-name--one { left: 50px; top: 175px; }
  .player-name--two { left: 296px; top: 155px; }

  .rounds {
    position: absolute; left: 26px; top: 205px; width: 371px; height: 450px;
    transform: rotate(-3deg); transform-origin: center;
    border-radius: 6px; overflow: hidden;
  }
  .round {
    position: relative; height: 90px;
    background: linear-gradient(180deg, var(--row-a), var(--row-b));
  }
  .round:nth-child(even) { background: linear-gradient(180deg, #5a1580, #4b0f6c); }
  .round__title {
    position: absolute; left: 0; right: 0; top: 12px; text-align: center;
    color: var(--round-text); font-size: 24px; font-weight: 600;
  }
  .round__category {
    position: absolute; left: 0; right: 0; top: 50px; text-align: center;
    color: var(--category-text); font-size: 18px; font-weight: 500;
  }
  .answers { position: absolute; top: 48px; display: flex; gap: 11px; }
  .answers--one { left: 36px; }
  .answers--two { left: 253px; top: 40px; }
  .answers svg { width: 22px; height: 24px; display: block; }
  .hex--green { fill: var(--hex-green); }
  .hex--red { fill: var(--hex-red); }
  .hex--empty { fill: none; stroke: var(--hex-empty); stroke-width: 1.3; }

  .footer-band {
    position: absolute; left: 0; right: 0; bottom: 0; height: 40px; background: var(--screen-foot);
  }
  .waiting-band {
    position: absolute; left: -10px; right: -10px; top: 645px; height: 80px;
    background: linear-gradient(90deg, #163238, #1b3b3f 50%, #163238);
    transform: rotate(-3deg);
  }
  .waiting-button {
    position: absolute; left: 90px; top: 656px; width: 246px; height: 56px;
    background: linear-gradient(180deg, var(--button-a), var(--button-b));
    border-radius: 4px; box-shadow: 0 4px 0 #a31c44;
    color: var(--button-text); font-size: 30px; font-weight: 700;
    text-align: center; line-height: 56px; transform: rotate(-3deg);
  }
</style>
</head>
<body>

<svg width="0" height="0" style="position:absolute">
  <defs>
    <polygon id="hex" points="11,1.5 20,6.5 20,17.5 11,22.5 2,17.5 2,6.5"/>
  </defs>
</svg>

<!-- Game overview screen -->
<section class="screen screen--left">
  <div class="status-bar">
    <svg width="48" height="10" viewBox="0 0 48 10"><g fill="#fff"><circle cx="4" cy="5" r="4"/><circle cx="14" cy="5" r="4"/><circle cx="24" cy="5" r="4"/></g><g fill="none" stroke="#fff"><circle cx="34" cy="5" r="3.5"/><circle cx="44" cy="5" r="3.5"/></g></svg>
    <svg class="status-bar__wifi" width="18" height="13" viewBox="0 0 18 13"><path d="M1 4.5a11.5 11.5 0 0 1 16 0M3.8 7.3a7.5 7.5 0 0 1 10.4 0M6.6 10a3.5 3.5 0 0 1 4.8 0" stroke="#fff" stroke-width="1.8" fill="none"/></svg>
    <span class="status-bar__time">4:21 PM</span>
    <span class="status-bar__battery">100%<svg width="34" height="13" viewBox="0 0 34 13"><rect x="0.5" y="0.5" width="30" height="12" rx="2" fill="none" stroke="#fff"/><rect x="2.5" y="2.5" width="26" height="8" fill="#fff"/><rect x="31.5" y="4" width="2" height="5" fill="#fff"/></svg></span>
  </div>

  <svg class="header-stripes" viewBox="0 0 423 60"><g stroke="var(--stripe)" stroke-width="2"><line x1="0" y1="50" x2="90" y2="44"/><line x1="0" y1="56" x2="90" y2="50"/><line x1="340" y1="14" x2="423" y2="8"/><line x1="340" y1="20" x2="423" y2="14"/><line x1="340" y1="26" x2="423" y2="20"/></g></svg>

  <div class="avatar avatar--one"><div class="avatar__portrait" role="img" aria-label="Player 1 character portrait"></div></div>
  <div class="scoreboard">
    <div class="score score--one">15</div>
    <div class="score-colon">:</div>
    <div class="score score--two">12</div>
  </div>
  <div class="avatar avatar--two"><div class="avatar__portrait" role="img" aria-label="Player 2 character portrait"></div></div>

  <div class="player-name player-name--one">Player 1</div>
  <div class="player-name player-name--two">Player 2</div>

  <div class="rounds">
    <div class="round">
      <div class="answers answers--one"><svg class="hex--red"><use href="#hex"/></svg><svg class="hex--green"><use href="#hex"/></svg><svg class="hex--red"><use href="#hex"/></svg></div>
      <div class="round__title">Round 1</div><div class="round__category">Category</div>
      <div class="answers answers--two"><svg class="hex--green"><use href="#hex"/></svg><svg class="hex--green"><use href="#hex"/></svg><svg class="hex--green"><use href="#hex"/></svg></div>
    </div>
    <div class="round">
      <div class="answers answers--one"><svg class="hex--green"><use href="#hex"/></svg><svg class="hex--red"><use href="#hex"/></svg><svg class="hex--green"><use href="#hex"/></svg></div>
      <div class="round__title">Round 2</div><div class="round__category">Category</div>
      <div class="answers answers--two"><svg class="hex--red"><use href="#hex"/></svg><svg class="hex--red"><use href="#hex"/></svg><svg class="hex--green"><use href="#hex"/></svg></div>
    </div>
    <div class="round">
      <div class="answers answers--one"><svg class="hex--empty"><use href="#hex"/></svg><svg class="hex--empty"><use href="#hex"/></svg><svg class="hex--empty"><use href="#hex"/></svg></div>
      <div class="round__title">Round 3</div><div class="round__category">Category</div>
      <div class="answers answers--two"><svg class="hex--empty"><use href="#hex"/></svg><svg class="hex--empty"><use href="#hex"/></svg><svg class="hex--empty"><use href="#hex"/></svg></div>
    </div>
    <div class="round">
      <div class="answers answers--one"><svg class="hex--empty"><use href="#hex"/></svg><svg class="hex--empty"><use href="#hex"/></svg><svg class="hex--empty"><use href="#hex"/></svg></div>
      <div class="round__title">Round 4</div><div class="round__category">Category</div>
      <div class="answers answers--two"><svg class="hex--empty"><use href="#hex"/></svg><svg class="hex--empty"><use href="#hex"/></svg><svg class="hex--empty"><use href="#hex"/></svg></div>
    </div>
    <div class="round">
      <div class="answers answers--one"><svg class="hex--empty"><use href="#hex"/></svg><svg class="hex--empty"><use href="#hex"/></svg><svg class="hex--empty"><use href="#hex"/></svg></div>
      <div class="round__title">Round 5</div><div class="round__category">Category</div>
      <div class="answers answers--two"><svg class="hex--empty"><use href="#hex"/></svg><svg class="hex--empty"><use href="#hex"/></svg><svg class="hex--empty"><use href="#hex"/></svg></div>
    </div>
  </div>

  <div class="footer-band"></div>
</section>

<!-- Game overview screen, waiting state -->
<section class="screen screen--right">
  <div class="status-bar">
    <svg width="48" height="10" viewBox="0 0 48 10"><g fill="#fff"><circle cx="4" cy="5" r="4"/><circle cx="14" cy="5" r="4"/><circle cx="24" cy="5" r="4"/></g><g fill="none" stroke="#fff"><circle cx="34" cy="5" r="3.5"/><circle cx="44" cy="5" r="3.5"/></g></svg>
    <svg class="status-bar__wifi" width="18" height="13" viewBox="0 0 18 13"><path d="M1 4.5a11.5 11.5 0 0 1 16 0M3.8 7.3a7.5 7.5 0 0 1 10.4 0M6.6 10a3.5 3.5 0 0 1 4.8 0" stroke="#fff" stroke-width="1.8" fill="none"/></svg>
    <span class="status-bar__time">4:21 PM</span>
    <span class="status-bar__battery">100%<svg width="34" height="13" viewBox="0 0 34 13"><rect x="0.5" y="0.5" width="30" height="12" rx="2" fill="none" stroke="#fff"/><rect x="2.5" y="2.5" width="26" height="8" fill="#fff"/><rect x="31.5" y="4" width="2" height="5" fill="#fff"/></svg></span>
  </div>

  <svg class="header-stripes" viewBox="0 0 423 60"><g stroke="var(--stripe)" stroke-width="2"><line x1="0" y1="50" x2="90" y2="44"/><line x1="0" y1="56" x2="90" y2="50"/><line x1="340" y1="14" x2="423" y2="8"/><line x1="340" y1="20" x2="423" y2="14"/><line x1="340" y1="26" x2="423" y2="20"/></g></svg>

  <div class="avatar avatar--one"><div class="avatar__portrait" role="img" aria-label="Player 1 character portrait"></div></div>
  <div class="scoreboard">
    <div class="score score--one">15</div>
    <div class="score-colon">:</div>
    <div class="score score--two">12</div>
  </div>
  <div class="avatar avatar--two"><div class="avatar__portrait" role="img" aria-label="Player 2 character portrait"></div></div>

  <div class="player-name player-name--one">Player 1</div>
  <div class="player-name player-name--two">Player 2</div>

  <div class="rounds">
    <div class="round">
      <div class="answers answers--one"><svg class="hex--red"><use href="#hex"/></svg><svg class="hex--green"><use href="#hex"/></svg><svg class="hex--red"><use href="#hex"/></svg></div>
      <div class="round__title">Round 1</div><div class="round__category">Category</div>
      <div class="answers answers--two"><svg class="hex--green"><use href="#hex"/></svg><svg class="hex--green"><use href="#hex"/></svg><svg class="hex--green"><use href="#hex"/></svg></div>
    </div>
    <div class="round">
      <div class="answers answers--one"><svg class="hex--green"><use href="#hex"/></svg><svg class="hex--red"><use href="#hex"/></svg><svg class="hex--green"><use href="#hex"/></svg></div>
      <div class="round__title">Round 2</div><div class="round__category">Category</div>
      <div class="answers answers--two"><svg class="hex--red"><use href="#hex"/></svg><svg class="hex--red"><use href="#hex"/></svg><svg class="hex--green"><use href="#hex"/></svg></div>
    </div>
    <div class="round">
      <div class="answers answers--one"><svg class="hex--empty"><use href="#hex"/></svg><svg class="hex--empty"><use href="#hex"/></svg><svg class="hex--empty"><use href="#hex"/></svg></div>
      <div class="round__title">Round 3</div><div class="round__category">Category</div>
      <div class="answers answers--two"><svg class="hex--empty"><use href="#hex"/></svg><svg class="hex--empty"><use href="#hex"/></svg><svg class="hex--empty"><use href="#hex"/></svg></div>
    </div>
    <div class="round">
      <div class="answers answers--one"><svg class="hex--empty"><use href="#hex"/></svg><svg class="hex--empty"><use href="#hex"/></svg><svg class="hex--empty"><use href="#hex"/></svg></div>
      <div class="round__title">Round 4</div><div class="round__category">Category</div>
      <div class="answers answers--two"><svg class="hex--empty"><use href="#hex"/></svg><svg class="hex--empty"><use href="#hex"/></svg><svg class="hex--empty"><use href="#hex"/></svg></div>
    </div>
    <div class="round">
      <div class="answers answers--one"><svg class="hex--empty"><use href="#hex"/></svg><svg class="hex--empty"><use href="#hex"/></svg><svg class="hex--empty"><use href="#hex"/></svg></div>
      <div class="round__title">Round 5</div><div class="round__category">Category</div>
      <div class="answers answers--two"><svg class="hex--empty"><use href="#hex"/></svg><svg class="hex--empty"><use href="#hex"/></svg><svg class="hex--empty"><use href="#hex"/></svg></div>
    </div>
  </div>

  <div class="footer-band"></div>
  <div class="waiting-band"></div>
  <div class="waiting-button">Waiting</div>
</section>

</body>
</html>
```